My Book needs a front and back cover design

I need you to design my front and back cover of my book. The title of my book is : Lanterns Past Harbour
Tide Notes
7 paths to gardening calmly always

The picture that I uploaded needs to be on the front cover. On the back cover it should be excerpt from Chapter One like this :

As years have gone by I have become much more conscious about my problem with stuttering, more able to relax my muscles to alleviate it. At the age of 20, I realized that stuttering is like a demon in my head that needs to be killed and that nothing is wrong with me. Furthermore, no one can help me but myself. I'm holding the key of my future. Everything is just in my head.

With this book, I want to help you realize that nobody can help you fix your stuttering better than yourself. There's no quick-get-rid-of-stuttering cure. The cure lies inside of you.

- Lorcan Vittel, excerpt from Chapter One
----------------------------------------------------------------------------------

My name also needs to be located on the front cover.

Target Market(s)

80 million people who stutter each day

Industry/Entity Type

Psychology

Font styles to use
Serif
Sans Serif

Colors
1b1b1b
000000
333333

Requirements
Must have
• Front Cover : Full Title and subtitle and my name and my picture
• Back Cover : Excerpt from my Chapter One with my name below just as I have described in my project description
Nice to have
• Maybe black background would be the best for the front cover.

```html
<!DOCTYPE html>
<html lang="en">
<head>
<meta charset="utf-8">
<title>Lanterns Past Harbour — Tide Notes · Book Cover</title>
<link rel="stylesheet" href="https://fonts.googleapis.com/css2?family=Fira+Sans:wght@400;500;600&family=Noto+Serif:ital@1&display=swap">
<style>
  :root {
    --ink-black: #000000;
    --ink-deep: #0b0b0b;
    --ink-soft: #1b1b1b;
    --ink-edge: #333333;
    --paper: #ffffff;
    --paper-grey: #e4e4e4;
    --fog-grey: #9a9a9a;
    --text-grey: #444444;
    --title-white: #f2f2f2;
    --sans: "Fira Sans", "Helvetica Neue", Arial, sans-serif;
    --serif: "Noto Serif", Georgia, serif;
  }
  * { margin: 0; padding: 0; box-sizing: border-box; }
  html, body { width: 1200px; height: 888px; overflow: hidden; background: var(--paper); }

  .cover-spread { position: relative; width: 1200px; height: 888px; }

  /* Back cover */
  .back-cover { position: absolute; left: 0; top: 0; width: 575px; height: 888px; }
  .back-cover__top {
    position: absolute; left: 0; top: 0; width: 100%; height: 153px;
    background: linear-gradient(to bottom, var(--paper) 0%, var(--paper-grey) 100%);
  }
  .back-cover__excerpt-band {
    position: absolute; left: 0; top: 153px; width: 100%; height: 380px;
    background: var(--paper);
    padding: 30px 26px 0;
    text-align: center;
  }
  .excerpt {
    font-family: var(--serif); font-style: italic; font-size: 13.2px;
    letter-spacing: 0.9px; line-height: 28.5px; color: var(--text-grey);
  }
  .excerpt + .excerpt { margin-top: 28px; }
  .excerpt-credit {
    margin-top: 14px; font-family: var(--serif); font-size: 14px; color: var(--text-grey);
  }
  .excerpt-credit em { font-size: 13px; }
  .back-cover__bottom {
    position: absolute; left: 0; top: 533px; width: 100%; height: 355px;
    background: linear-gradient(to bottom, var(--fog-grey) 0%, #cfcfcf 60%, var(--paper) 100%);
  }

  /* Spine */
  .spine {
    position: absolute; left: 575px; top: 0; width: 50px; height: 888px;
    background: var(--ink-black);
  }
  .spine__text {
    position: absolute; left: 25px; top: 44px;
    transform-origin: 0 0; transform: rotate(90deg) translateY(-50%);
    white-space: nowrap;
    font-family: var(--sans); font-weight: 500; font-size: 15.5px; letter-spacing: 1px;
    color: var(--title-white);
  }
  .spine__author { margin-left: 14px; letter-spacing: 1.2px; }

  /* Front cover */
  .front-cover {
    position: absolute; left: 625px; top: 0; width: 575px; height: 888px;
    background: var(--ink-edge);
  }
  .author-portrait {
    position: absolute; left: 50px; top: 0; width: 475px; height: 888px;
    background:
      radial-gradient(ellipse 55% 40% at 52% 30%, #3a3430 0%, #161414 55%, transparent 80%),
      radial-gradient(ellipse 70% 60% at 50% 70%, #141414 0%, var(--ink-deep) 70%),
      var(--ink-black);
  }
  .front-title {
    position: absolute; left: 50px; width: 475px; text-align: center;
    font-family: var(--sans); color: var(--title-white); text-transform: uppercase;
    line-height: 1;
  }
  .front-title__line1 { top: 552px; font-size: 44px; font-weight: 500; letter-spacing: 1px; }
  .front-title__line2 { top: 604px; font-size: 60px; font-weight: 500; letter-spacing: 1px; }
  .front-title__series { top: 666px; font-size: 78px; font-weight: 400; letter-spacing: 2px; color: #e6e6e6; }
  .front-subtitle {
    position: absolute; left: 50px; width: 475px; top: 748px; text-align: center;
    font-family: var(--sans); font-size: 26px; color: var(--title-white);
  }
  .front-author {
    position: absolute; right: 50px; top: 806px;
    font-family: var(--sans); font-weight: 600; font-size: 24px; letter-spacing: 1px;
    color: var(--title-white);
  }
</style>
</head>
<body>
<main class="cover-spread">

  <section class="back-cover">
    <div class="back-cover__top"></div>
    <div class="back-cover__excerpt-band">
      <p class="excerpt">As years have gone by I have become much more conscious about my problem with stuttering, more able to relax my muscles to alleviate it. At the age of 20, I realized that stuttering is like a demon in my head that needs to be killed and that nothing is wrong with me. Furthermore, no one can help me but myself. I'm holding the key of my future. Everything is just in my head.</p>
      <p class="excerpt">With this book, I want to help you realize that nobody can help you fix your stuttering better than yourself. There's no quick-get-rid-of-stuttering cure. The cure lies inside of you.</p>
      <p class="excerpt-credit">- Lorcan Vittel, <em>excerpt from Chapter One</em></p>
    </div>
    <div class="back-cover__bottom"></div>
  </section>

  <aside class="spine">
    <div class="spine__text">LANTERNS PAST HARBOUR: TIDE NOTES. 7 Paths to gardening calmly always <span class="spine__author">LORCAN VITTEL</span></div>
  </aside>

  <section class="front-cover">
    <div class="author-portrait" role="img" aria-label="Portrait photograph of the author in a dark polo shirt standing against a black backdrop"></div>
    <h1 class="front-title front-title__line1">Lanterns Past</h1>
    <p class="front-title front-title__line2">Harbour</p>
    <p class="front-title front-title__series">Tide Notes</p>
    <p class="front-subtitle">7 paths to gardening calmly always</p>
    <p class="front-author">LORCAN VITTEL</p>
  </section>

</main>
</body>
</html>
```